Brochure for luxury baby clothing

We need a square (5.5') catalog/brochure to market our baby clothing to baby stores. We offer baby clothing made of 100% peruvian pima cotton, world's finest and softest cotton. The online store was launched 2 months ago in Canada and we are now going to market the clothing to stores across Canada. We are looking to have a beautiful catalog to present the products to potential buyers (store owners and managers)
Catalog will be presented in print but we may also use a table to present it
Selected designer to provide source document (illustrator)

Target Market(s)

Baby stores and department stores across Canada (store owners, buyers and managers)

Industry/Entity Type

Baby

Requirements
Must have
• - Cover
• - Pages 2 – 3. About us section
• o 2: Nice image resembling softness, exclusive, luxury, cozy... and perhaps a phase: "Pure softness for babies..."
• o 3: About Little Lumo Nest and about Pima Cotton (content in our website: www.littlelumo.ca)
• - Pages 4-5: Newborn section. Picture of a baby wearing our clothing and pictures and short descriptions of some products
• - Pages 6-7: Girls section. Picture of a girl wearing our clothing and pictures and short descriptions of some products
• - Pages 8-9: Boys section. Picture of a boy wearing our clothing and pictures and short descriptions of some products
• - Page 10. Organics section. Pictures and short descriptions of some products
• - Page 11. Accessories. Pictures and short descriptions of some products
• - Back. Logo and contact information (email, phone, facebook, Instagram)

```html
<!DOCTYPE html>
<html lang="en">
<head>
<meta charset="utf-8">
<title>Little Lumo Nest – Brochure Covers</title>
<link href="https://fonts.googleapis.com/css2?family=Cabin:wght@400;500&display=swap" rel="stylesheet">
<style>
  :root {
    --backdrop: #ebe6e1;
    --cover-blue: #a9c5e1;
    --cover-blue-light: #bcd3ea;
    --photo-dark: #4f4a49;
    --photo-mid: #7b706d;
    --photo-light: #9a8f8b;
    --brand-taupe: #7a6d64;
    --text-light: #f2eeea;
    --badge-white: #f7f5f2;
  }
  * { margin: 0; padding: 0; box-sizing: border-box; }
  html, body {
    width: 1200px; height: 880px; overflow: hidden;
    background: var(--backdrop);
    font-family: "Cabin", sans-serif;
  }
  .spread {
    position: absolute; left: 80px; top: 180px;
    width: 1040px; height: 520px;
    display: flex;
    box-shadow: 0 10px 30px rgba(0,0,0,.18);
  }
  .back-cover, .front-cover {
    position: relative; width: 520px; height: 520px;
  }
  .back-photo {
    position: absolute; inset: 0;
    background:
      linear-gradient(180deg, rgba(40,36,35,.35) 0%, rgba(40,36,35,.1) 55%, rgba(40,36,35,.25) 100%),
      linear-gradient(120deg, var(--photo-dark) 0%, var(--photo-mid) 45%, var(--photo-light) 75%, var(--photo-mid) 100%);
  }
  .back-contact {
    position: absolute; left: 0; right: 0; top: 268px;
    display: flex; flex-direction: column; align-items: center; gap: 10px;
    color: var(--text-light);
  }
  .brand-mark {
    display: flex; align-items: center; gap: 8px;
    font-weight: 500; color: var(--brand-taupe);
  }
  .brand-mark .dot {
    border-radius: 50%; background: var(--badge-white);
  }
  .brand-mark--stacked {
    flex-direction: column; gap: 6px;
    color: var(--text-light); font-size: 16px;
    margin-bottom: 4px;
  }
  .brand-mark--stacked .dot { width: 36px; height: 36px; }
  .contact-line { font-size: 15px; letter-spacing: .3px; }
  .social-row { display: flex; gap: 40px; font-size: 13px; }
  .social-item { display: flex; align-items: center; gap: 7px; }
  .social-icon { width: 15px; height: 15px; flex: none; }
  .front-cover {
    background: linear-gradient(160deg, var(--cover-blue) 0%, var(--cover-blue-light) 60%, var(--cover-blue) 100%);
    display: flex; align-items: center; justify-content: center;
    border-left: 1px solid rgba(0,0,0,.08);
  }
  .front-cover .brand-mark { font-size: 34px; gap: 14px; }
  .front-cover .brand-mark .dot { width: 34px; height: 34px; }
</style>
</head>
<body>
  <main class="spread">
    <section class="back-cover">
      <div class="back-photo" role="img" aria-label="Dimmed photo of soft baby clothing hanging on a rail"></div>
      <div class="back-contact">
        <div class="brand-mark brand-mark--stacked"><span class="dot"></span><span>Little Lumo Nest</span></div>
        <p class="contact-line">info@littlelumo.ca | (416) 555-0142</p>
        <div class="social-row">
          <span class="social-item">
            <svg class="social-icon" viewBox="0 0 16 16" aria-hidden="true" fill="none" stroke="currentColor" stroke-width="1.2">
              <circle cx="8" cy="8" r="6.5"/>
              <ellipse cx="8" cy="8" rx="3" ry="6.5"/>
              <line x1="1.5" y1="8" x2="14.5" y2="8"/>
            </svg>littlelumo.ca</span>
          <span class="social-item">
            <svg class="social-icon" viewBox="0 0 16 16" aria-hidden="true" fill="none" stroke="currentColor" stroke-width="1.2">
              <circle cx="8" cy="8" r="2.6"/>
              <path d="M10.6 5.6v3.3c0 1.4 2.9 1.6 2.9-1A5.6 5.6 0 1 0 11 12.6"/>
            </svg>littlelumonest</span>
        </div>
      </div>
    </section>
    <section class="front-cover">
      <div class="brand-mark"><span class="dot"></span><span>Little Lumo Nest</span></div>
    </section>
  </main>
</body>
</html>
```